dealcraftmentor.com - Podcast Guest Marketing E-Flyer PDF

Dear Designers:I am in need of an attractive and attention-getting layout and design for a three-page marketing flyer (commonly known as a media one sheet) that will be sent via e-mail, as PDF file, to various Podcast hosts to market me as a guest on their podcasts. I want the design of the document to "mirror" the design and branding on my parent dealcraftmentor.com website. I am providing ALL the edited and proofread copy and content - the designer just needs to create the design for this marketing document. I want an active PDF document and icons should be used for WorkLoop, Phone, E-mail , and website- with hyperlinks that connect accordingly. I need a fast turnaround.
Updates

Dear Designers - instead of using the photo in the project file of me speaking to the audience for the banner image - I thought it would be a better idea to make this marketing piece specific to Podcast Hosts. Therefore, an image such as the one in the link below would be good to use for a banner image. https://www.pixelvarnow.com/find?q=podcast+studio+photos&mode=img&ref=univ&id=Qm7TzRk2LwPa9XcNvB4eHyU8sDjF1gA5oE3iKtZ6bW0nMh&w=1377&h=804#pic=vrolapemxq3BcT:

Target Market(s)

This PDF document will be sent to 650 Podcast hosts in North America via a broadcast e-mail.

Font styles to use
Sans Serif

Colors
ec1f27
ffffff
000000
333333
9d9d9d

Requirements
Must have
• A three-page layout that is easy to navigate in PDF form.
• Proper font styles and sizes for key emphasis areas on the document/
• Consistent branding to mirror my dealcraftmentor.com parent website
• Must be easy for people to read
• Attention-getting design elements and layout
• Professional and sophisticated design
• Icons for contact information
Should not have
• Should not be cluttered and junky-looking.
• Should not use small font sizes that makes it difficult to read.
• If Podcast hosts are interested in having me as a guest - they will read the content as required on three-pages

```html
<!DOCTYPE html>
<html lang="en">
<head>
<meta charset="utf-8">
<title>Daniel R. Kestrow – Podcast Guest One Sheet</title>
<link rel="stylesheet" href="https://fonts.googleapis.com/css2?family=Montserrat:wght@300;400;500&family=Rubik:wght@500;700&display=swap">
<style>
  :root{
    --brand-red:#ec1f27;
    --deep-red:#a50d1d;
    --white:#ffffff;
    --ink:#000000;
    --text:#333333;
    --muted:#9d9d9d;
    --panel-dark:#6b6b6b;
    --panel-light:#f1f1f1;
  }
  *{margin:0;padding:0;box-sizing:border-box}
  html,body{width:849px;height:1200px;overflow:hidden;background:var(--white)}
  body{font-family:"Montserrat",sans-serif;color:var(--text);position:relative}
  .brand{position:absolute;left:62px;top:66px;display:flex;align-items:center;gap:8px}
  .brand-mark{width:22px;height:22px;background:var(--brand-red)}
  .brand-name{font-family:"Montserrat",sans-serif;font-weight:400;font-size:26px;letter-spacing:-0.8px;color:var(--text)}
  .hero{position:absolute;left:0;top:127px;width:849px;height:557px;border-top-right-radius:110px;overflow:hidden}
  .hero-photo{position:absolute;inset:0;background:linear-gradient(160deg,#d6202b 0%,#e31e2a 45%,#d31825 75%,#c8131f 100%)}
  .hero-title{position:absolute;left:0;top:0;width:100%;height:118px;background:var(--deep-red);padding:8px 0 0 58px;color:var(--white)}
  .hero-title h1{font-weight:300;font-size:57px;line-height:64px;letter-spacing:0.5px}
  .hero-title h2{font-weight:500;font-size:25px;line-height:30px;margin-top:6px}
  .reasons{position:absolute;left:57px;top:138px;width:720px;list-style:none;color:var(--white);font-size:14.6px;font-weight:300;line-height:18.6px}
  .reasons li{position:relative;padding-left:17px;text-align:justify;margin-bottom:10.8px}
  .reasons li span{position:absolute;left:0;top:0}
  .benefit{position:absolute;left:57px;top:715px;width:426px}
  .benefit h3{font-family:"Rubik",sans-serif;font-weight:700;font-size:29px;line-height:34px;color:var(--brand-red);margin-bottom:14px}
  .benefit p{font-size:14.6px;font-weight:300;line-height:19.3px;text-align:justify;color:var(--text);margin-bottom:11px}
  .media-head{position:absolute;left:540px;top:798px;width:309px;height:136px;background:var(--panel-dark);color:var(--white);padding:19px 0 0 14px}
  .media-head h4{font-weight:500;font-size:20px;line-height:24px}
  .media-head p{font-size:12.8px;font-weight:300;line-height:17px;margin-top:8px}
  .media-list{position:absolute;left:540px;top:934px;width:309px;height:204px;background:var(--panel-light);display:grid;grid-template-columns:1fr 1fr;align-items:center;justify-items:center;padding:10px 8px}
  .outlet{font-family:"Montserrat",sans-serif;font-weight:500;font-size:19px;color:#5a5a5a;display:flex;align-items:center;gap:6px}
  .outlet i{display:block;width:12px;height:12px;background:#5a5a5a}
</style>
</head>
<body>
  <div class="brand"><div class="brand-mark"></div><div class="brand-name">dealcraftmentor</div></div>

  <section class="hero">
    <div class="hero-photo" role="img" aria-label="Red-toned photo of a seated audience at a speaking event"></div>
    <div class="hero-title">
      <h1>Six Reasons</h1>
      <h2>to Book Daniel R. Kestrow As a Guest on Your Podcast</h2>
    </div>
    <ol class="reasons">
      <li><span>1.</span>Daniel is a dynamic, thought-provoking, engaging, captivating, and entertaining speaker who will share some great personal stories to help your listeners better understand and relate to the topic of negotiating and decision-making dynamics. He will indeed challenge the “status quo.”</li>
      <li><span>2.</span>Daniel is the founder of dealcraftmentor.com® and is an internationally recognized expert and highly rated speaker on the topics of negotiating and decision-making dynamics that affect negotiated outcomes. His versatility and commitment to proper preparation will ensure that his content is tailored to address the theme of your podcast and the needs of your listeners.</li>
      <li><span>3.</span>His five-star-rated presentations and training programs have been delivered around the world to small and medium-sized businesses, Top 500 corporations, and large industry, trade, and peer-to-peer associations such as Rising Chiefs Network and Founders’ Circle Alliance.</li>
      <li><span>4.</span>Daniel has personally trained over 50,000 people of all experience levels, across multiple industries, in 31 countries how to negotiate more effectively.</li>
      <li><span>5.</span>With formal training in broadcasting and media arts, Daniel provides 30 years of experience as a professional speaker who can provide your listeners with valuable insights, solutions, and answers to address listeners’ challenges and questions.</li>
      <li><span>6.</span>Daniel is the creator of the best-selling Deal Mastery Audio Learning Program – designed to be an effective all-in-one learning solution that helps people improve their negotiating capabilities and skills. He is also the host of his soon-to-be-launched Podcast – The Deal Table.</li>
    </ol>
  </section>

  <section class="benefit">
    <h3>How Podcast Listeners<br>Will Benefit?</h3>
    <p>Most people are intimidated by the prospect and process of negotiating – and often view negotiating as an uncomfortable haggling and bargaining process that may involve confrontation, anxiety, and stress.</p>
    <p>If podcast listeners are like most people – then they probably are concerned about being taken advantage of – or that they are missing out on potential opportunities in their personal, social, and business negotiations.</p>
    <p>To alleviate your listeners’ concerns, Daniel will provide them with easy-to-understand negotiating strategies, tactics, phrases, and tips they can immediately apply – the moment the podcast episode ends. Your listeners will feel more confident when they are equipped with the powerful and beneficial strategies and techniques that will help them save/make money and arrive at better outcomes when negotiating with customers, clients, suppliers, contractors, financial institutions, retailers, co-workers, colleagues, and family members.</p>
  </section>

  <aside>
    <div class="media-head">
      <h4>Daniel R. Kestrow<br>in the Media</h4>
      <p>Daniel has appeared on radio programs, written articles or contributed to articles for the following media outlets:</p>
    </div>
    <div class="media-list">
      <div class="outlet"><i></i>Northern Ledger</div>
      <div class="outlet">SalesPulse</div>
      <div class="outlet">Marketwise.com</div>
      <div class="outlet">Vantage</div>
      <div class="outlet">Margin</div>
      <div class="outlet"><i></i>OpenDesk</div>
    </div>
  </aside>
</body>
</html>
```